VLM8 Business Card Design Project

Design which catches the client with the first impression. A design which is professional and classy with elegance. We have also got another project running and the winning prize for that is $240 "vlm8 print + graphic design".
For all the company details please visit www.vlm8-example.com.
Please find the logo attached and i would like to have good colors for my business card.
, Design which catches the client with the first impression. A design which is professional and classy with elegance.
Updates
VLM8 is running two projects at the same time, please feel free to participate. The other project name is

```html
<!DOCTYPE html>
<html lang="en">
<head>
<meta charset="utf-8">
<title>VLM8 Business Card</title>
<link rel="stylesheet" href="https://fonts.googleapis.com/css2?family=Mulish:wght@400;700;800&display=swap">
<style>
  :root {
    --backdrop: #d9d4cc;
    --card: #000000;
    --teal: #45b386;
    --lime: #bbd600;
  }
  html, body {
    margin: 0;
    padding: 0;
    width: 1200px;
    height: 1000px;
    overflow: hidden;
    background: var(--backdrop);
    font-family: "Mulish", Arial, sans-serif;
  }
  .canvas {
    position: relative;
    width: 1200px;
    height: 1000px;
  }
  .card {
    position: absolute;
    left: 200px;
    width: 800px;
    height: 430px;
    background: var(--card);
    border-radius: 30px;
    box-shadow: 0 14px 30px rgba(0,0,0,0.25);
    overflow: hidden;
  }
  .card--front { top: 50px; }
  .card--back { top: 520px; }

  .brand {
    position: absolute;
    left: 0;
    right: 0;
    top: 0;
    bottom: 0;
    display: flex;
    align-items: center;
    justify-content: center;
    gap: 28px;
  }
  .brand__dot {
    width: 64px;
    height: 64px;
    border-radius: 50%;
    background: var(--lime);
  }
  .brand__name {
    font-size: 128px;
    font-weight: 800;
    letter-spacing: 4px;
    color: var(--teal);
    line-height: 1;
  }

  .holder {
    position: absolute;
    left: 260px;
    top: 140px;
    text-align: center;
    color: var(--teal);
  }
  .holder__name {
    font-size: 44px;
    font-weight: 800;
    margin: 0;
    line-height: 1.1;
  }
  .holder__role {
    font-size: 32px;
    font-weight: 400;
    margin: 6px 0 0;
  }

  .contact {
    position: absolute;
    left: 42px;
    bottom: 48px;
    list-style: none;
    margin: 0;
    padding: 0;
    color: var(--teal);
    font-size: 16px;
  }
  .contact__item {
    display: flex;
    align-items: center;
    gap: 16px;
    margin-top: 14px;
  }
  .contact__icon {
    width: 22px;
    height: 22px;
    flex: none;
  }
  .accent-dot {
    position: absolute;
    right: 44px;
    top: 44px;
    width: 64px;
    height: 64px;
    border-radius: 50%;
    background: var(--lime);
  }
</style>
</head>
<body>
<main class="canvas">

  <section class="card card--front" aria-label="Card front">
    <div class="brand">
      <span class="brand__dot"></span>
      <span class="brand__name">VLM8</span>
    </div>
  </section>

  <section class="card card--back" aria-label="Card back">
    <span class="accent-dot"></span>
    <div class="holder">
      <h1 class="holder__name">Marlo Venn</h1>
      <p class="holder__role">Managing Director</p>
    </div>
    <ul class="contact">
      <li class="contact__item">
        <svg class="contact__icon" viewBox="0 0 24 24" fill="none" stroke="currentColor" stroke-width="1.6">
          <rect x="6.5" y="2" width="11" height="20" rx="2"/>
          <line x1="10.5" y1="18.5" x2="13.5" y2="18.5"/>
        </svg>
        <span>5550142867</span>
      </li>
      <li class="contact__item">
        <svg class="contact__icon" viewBox="0 0 24 24" fill="none" stroke="currentColor" stroke-width="1.6">
          <rect x="2" y="5" width="20" height="14" rx="1"/>
          <polyline points="2,5 12,13 22,5"/>
        </svg>
        <span>hello@vlm8-example.com</span>
      </li>
    </ul>
  </section>

</main>
</body>
</html>
```